Flat Belly Design Graphics for Social

I want to create 9 social media graphics (new Instagram size 4:5 (1080 x 1350 pixels) focusing on our Flat Belly Graphics, using the pics attached. Use the attached pics, NO RANDOM STOCK PHOTOGRAPHY. For the color scheme of the graphics, the color palette is attached. YOU MUST POST ALL 9 GRAPHICS IN ONE ENTRY.
Using the 3 titles below, create one set of graphics. 1) with all text, then for the others, use the pictures as detailed below in IMPORTANT:
1. 21-Night Lean Middle Reboot Beyond 50
2. The 20-Second Trim-Core Menu Guide
3. Starlet Tricks to a Slender Midline Beyond 50 - Zero Scalpel Needed
IMPORTANT:
Only use RK Pic 1 and RK Pic 2 with the title, 21-Night Lean Middle Reboot Beyond 50
Only use meal plan1 and meal plan2 pics with the title, 20-Second Trim-Core Menu Guide
Only use starlet tricks 1 and starlet tricks 2 pics with the title, Starlet Tricks to a Slender Midline Beyond 50 - Zero Scalpel Needed
women over 40

```html
<!DOCTYPE html>
<html lang="en">
<head>
<meta charset="utf-8">
<title>Lean Middle Social Set</title>
<link rel="stylesheet" href="https://fonts.googleapis.com/css2?family=Poppins:wght@500;600;700;800&family=Yellowtail&display=swap">
<style>
  :root{
    --rose:#e398ae;
    --rose-deep:#d97f9b;
    --petal:#f5d6dd;
    --blush:#f2cdd6;
    --paper:#fbeef1;
    --ink:#2f4a45;
    --ink-deep:#1f3531;
    --script:#e693ad;
    --white:#ffffff;
    --rb-band:#eba7ba;
    --rb-tail:#e496ac;
    --rb-fold:#c9718d;
    --rb-text:#ffffff;
  }
  *{box-sizing:border-box;margin:0;padding:0}
  html,body{width:1008px;height:1200px;overflow:hidden;background:var(--white)}
  .canvas{position:relative;width:1008px;height:1200px;background:var(--white);font-family:"Poppins",sans-serif}

  .card{position:absolute;width:283px;height:353px;overflow:hidden}
  .col-1{left:43px}.col-2{left:362px}.col-3{left:681px}
  .row-1{top:33px}.row-2{top:423px}.row-3{top:813px}

  .card--bordered{border:7px solid var(--rose);background:radial-gradient(ellipse at 50% 25%,var(--white) 0%,var(--paper) 45%,var(--blush) 100%)}
  .card--framed{background:var(--petal)}
  .card--framed .frame{position:absolute;inset:12px;border:3px solid var(--white);background:linear-gradient(160deg,var(--blush) 0%,var(--paper) 45%,var(--blush) 100%)}
  .card--banded{background:var(--petal)}
  .band{position:absolute;left:7px;right:7px;background:var(--rose)}

  .photo{position:absolute}
  .photo--portrait{background:radial-gradient(ellipse at 50% 55%,#f3e6e3 0%,#e7cfc9 45%,rgba(242,205,214,0) 75%)}
  .photo--meals{background:linear-gradient(135deg,#7a4a2c 0%,#4a3426 40%,#6b8a3a 70%,#c8513a 100%)}

  .ln{position:absolute;left:0;right:0;text-align:center;transform:translateY(-50%);white-space:nowrap;line-height:1}
  .head{font-weight:800;color:var(--ink);letter-spacing:.5px}
  .sub{font-weight:500;color:var(--ink)}
  .on-band{color:var(--white)}
  .script{font-family:"Yellowtail",cursive;color:var(--script);font-weight:400}
  .script.on-band{color:#f8dbe3}

  .ruled{display:flex;justify-content:center;align-items:center;gap:4px}
  .ruled::before,.ruled::after{content:"";display:block;height:2px;background:currentColor;width:var(--rule,48px)}

  .ribbon{position:absolute}
  .ribbon svg{position:absolute;inset:0;width:100%;height:100%}
  .ribbon .tail{fill:var(--rb-tail)}
  .ribbon .fold{fill:var(--rb-fold)}
  .ribbon .band-fill{fill:var(--rb-band)}
  .ribbon span{position:absolute;left:13%;right:13%;top:0;height:80%;display:flex;align-items:center;justify-content:center;font-weight:700;color:var(--rb-text);white-space:nowrap;letter-spacing:.5px}
  .ribbon--ink{--rb-band:var(--ink);--rb-tail:var(--ink);--rb-fold:var(--ink-deep)}

  .tag{position:absolute;left:48px;right:48px;display:flex;align-items:center;justify-content:center;font-weight:700;font-size:12.5px;color:var(--ink);letter-spacing:.3px}
  .tag--outline{border:1px solid var(--ink)}
  .tag--solid{background:var(--white)}
  .rule-white{position:absolute;left:12px;right:12px;height:3px;background:var(--white)}
</style>
</head>
<body>
<main class="canvas">

  <!-- Set 1: 21-Night Lean Middle Reboot -->
  <section class="card card--bordered col-1 row-1">
    <div class="photo photo--portrait" style="left:58px;top:14px;width:154px;height:166px" role="img" aria-label="Smiling woman in a cropped white sweater pointing to her toned midsection"></div>
    <div class="ribbon" style="left:24px;top:180px;width:222px;height:60px">
      <svg viewBox="0 0 200 50" preserveAspectRatio="none" aria-hidden="true">
        <polygon class="tail" points="2,12 40,12 40,48 2,48 12,30"/><polygon class="fold" points="26,40 40,40 40,48"/>
        <polygon class="tail" points="198,12 160,12 160,48 198,48 188,30"/><polygon class="fold" points="174,40 160,40 160,48"/>
        <rect class="band-fill" x="26" y="0" width="148" height="40"/>
      </svg>
      <span style="font-size:19px">21-NIGHT</span>
    </div>
    <div class="ln sub" style="top:237px;font-size:27px">LEAN</div>
    <div class="ln head" style="top:270px;font-size:27px">MIDDLE REBOOT</div>
    <div class="ln script" style="top:303px;font-size:23px">Beyond 50</div>
  </section>

  <section class="card card--framed col-2 row-1">
    <div class="frame"></div>
    <div class="ribbon" style="left:40px;top:64px;width:203px;height:43px">
      <svg viewBox="0 0 200 50" preserveAspectRatio="none" aria-hidden="true">
        <polygon class="tail" points="2,12 40,12 40,48 2,48 12,30"/><polygon class="fold" points="26,40 40,40 40,48"/>
        <polygon class="tail" points="198,12 160,12 160,48 198,48 188,30"/><polygon class="fold" points="174,40 160,40 160,48"/>
        <rect class="band-fill" x="26" y="0" width="148" height="40"/>
      </svg>
      <span style="font-size:20px">21-NIGHT</span>
    </div>
    <div class="ln sub ruled" style="top:130px;font-size:27px;--rule:50px">LEAN</div>
    <div class="ln head" style="top:176px;font-size:42px">MIDDLE</div>
    <div class="ln head" style="top:226px;font-size:42px">REBOOT</div>
    <div class="ln script" style="top:280px;font-size:36px">Beyond 50</div>
  </section>

  <section class="card card--banded col-3 row-1">
    <div class="band" style="top:7px;height:123px"></div>
    <div class="band" style="top:255px;height:91px"></div>
    <div class="ribbon ribbon--ink" style="left:40px;top:42px;width:203px;height:43px">
      <svg viewBox="0 0 200 50" preserveAspectRatio="none" aria-hidden="true">
        <polygon class="tail" points="2,12 40,12 40,48 2,48 12,30"/><polygon class="fold" points="26,40 40,40 40,48"/>
        <polygon class="tail" points="198,12 160,12 160,48 198,48 188,30"/><polygon class="fold" points="174,40 160,40 160,48"/>
        <rect class="band-fill" x="26" y="0" width="148" height="40"/>
      </svg>
      <span style="font-size:20px">21-NIGHT</span>
    </div>
    <div class="ln sub on-band ruled" style="top:104px;font-size:22px;--rule:48px">LEAN</div>
    <div class="ln head" style="top:170px;font-size:42px">MIDDLE</div>
    <div class="ln head" style="top:221px;font-size:42px">REBOOT</div>
    <div class="ln script on-band" style="top:296px;font-size:36px">Beyond 50</div>
  </section>

  <!-- Set 2: The 20-Second Trim-Core Menu Guide -->
  <section class="card card--bordered col-1 row-2" style="background:var(--petal)">
    <div class="photo photo--meals" style="left:0;top:0;width:269px;height:181px" role="img" aria-label="Overhead view of fresh vegetables, fruit, salmon and eggs around a menu notebook on a dark wooden table"></div>
    <div class="ribbon" style="left:26px;top:150px;width:222px;height:60px">
      <svg viewBox="0 0 200 50" preserveAspectRatio="none" aria-hidden="true">
        <polygon class="tail" points="2,12 40,12 40,48 2,48 12,30"/><polygon class="fold" points="26,40 40,40 40,48"/>
        <polygon class="tail" points="198,12 160,12 160,48 198,48 188,30"/><polygon class="fold" points="174,40 160,40 160,48"/>
        <rect class="band-fill" x="26" y="0" width="148" height="40"/>
      </svg>
      <span style="font-size:15px">THE 20-SECOND</span>
    </div>
    <div class="ln head" style="top:229px;font-size:46px">TRIM-</div>
    <div class="ln head ruled" style="top:279px;font-size:46px;--rule:48px;margin-left:-7px">CORE</div>
    <div class="ln script" style="top:318px;font-size:24px">Menu Guide</div>
  </section>

  <section class="card card--framed col-2 row-2">
    <div class="frame"></div>
    <div class="ln sub ruled" style="top:68px;font-size:15px;--rule:28px">THE</div>
    <div class="ribbon" style="left:40px;top:82px;width:203px;height:42px">
      <svg viewBox="0 0 200 50" preserveAspectRatio="none" aria-hidden="true">
        <polygon class="tail" points="2,12 40,12 40,48 2,48 12,30"/><polygon class="fold" points="26,40 40,40 40,48"/>
        <polygon class="tail" points="198,12 160,12 160,48 198,48 188,30"/><polygon class="fold" points="174,40 160,40 160,48"/>
        <rect class="band-fill" x="26" y="0" width="148" height="40"/>
      </svg>
      <span style="font-size:19px">20-SECOND</span>
    </div>
    <div class="ln head" style="top:165px;font-size:52px">TRIM-</div>
    <div class="ln head" style="top:224px;font-size:52px">CORE</div>
    <div class="ln script" style="top:280px;font-size:30px">Menu Guide</div>
  </section>

  <section class="card card--banded col-3 row-2">
    <div class="band" style="top:7px;height:122px"></div>
    <div class="band" style="top:255px;height:91px"></div>
    <div class="ln sub on-band ruled" style="top:55px;font-size:15px;--rule:28px">THE</div>
    <div class="ribbon ribbon--ink" style="left:40px;top:71px;width:203px;height:42px">
      <svg viewBox="0 0 200 50" preserveAspectRatio="none" aria-hidden="true">
        <polygon class="tail" points="2,12 40,12 40,48 2,48 12,30"/><polygon class="fold" points="26,40 40,40 40,48"/>
        <polygon class="tail" points="198,12 160,12 160,48 198,48 188,30"/><polygon class="fold" points="174,40 160,40 160,48"/>
        <rect class="band-fill" x="26" y="0" width="148" height="40"/>
      </svg>
      <span style="font-size:19px">20-SECOND</span>
    </div>
    <div class="ln head" style="top:168px;font-size:46px">TRIM-</div>
    <div class="ln head" style="top:218px;font-size:46px">CORE</div>
    <div class="ln script on-band" style="top:295px;font-size:38px;color:var(--white)">Menu Guide</div>
  </section>

  <!-- Set 3: Starlet Tricks to a Slender Midline -->
  <section class="card card--bordered col-1 row-3" style="background:var(--petal)">
    <div class="ln head" style="top:59px;font-size:40px">STARLET</div>
    <div class="ln head" style="top:108px;font-size:40px">TRICKS</div>
    <div class="ln sub ruled" style="top:151px;font-size:17px;--rule:50px">TO A</div>
    <div class="ribbon" style="left:24px;top:180px;width:222px;height:58px">
      <svg viewBox="0 0 200 50" preserveAspectRatio="none" aria-hidden="true">
        <polygon class="tail" points="2,12 40,12 40,48 2,48 12,30"/><polygon class="fold" points="26,40 40,40 40,48"/>
        <polygon class="tail" points="198,12 160,12 160,48 198,48 188,30"/><polygon class="fold" points="174,40 160,40 160,48"/>
        <rect class="band-fill" x="26" y="0" width="148" height="40"/>
      </svg>
      <span style="font-size:15px">SLENDER MIDLINE</span>
    </div>
    <div class="ln script" style="top:241px;font-size:26px">Beyond 50</div>
    <div class="tag tag--outline" style="top:269px;height:27px;left:42px;right:42px">ZERO SCALPEL NEEDED</div>
  </section>

  <section class="card card--framed col-2 row-3">
    <div class="frame"></div>
    <div class="rule-white" style="top:284px"></div>
    <div class="ln head" style="top:66px;font-size:40px">STARLET</div>
    <div class="ln head" style="top:116px;font-size:40px">TRICKS</div>
    <div class="ln sub ruled" style="top:160px;font-size:17px;--rule:50px">TO A</div>
    <div class="ribbon" style="left:40px;top:184px;width:203px;height:42px">
      <svg viewBox="0 0 200 50" preserveAspectRatio="none" aria-hidden="true">
        <polygon class="tail" points="2,12 40,12 40,48 2,48 12,30"/><polygon class="fold" points="26,40 40,40 40,48"/>
        <polygon class="tail" points="198,12 160,12 160,48 198,48 188,30"/><polygon class="fold" points="174,40 160,40 160,48"/>
        <rect class="band-fill" x="26" y="0" width="148" height="40"/>
      </svg>
      <span style="font-size:14px">SLENDER MIDLINE</span>
    </div>
    <div class="ln script" style="top:245px;font-size:26px">Beyond 50</div>
    <div class="tag tag--solid" style="top:272px;height:27px;left:48px;right:48px">ZERO SCALPEL NEEDED</div>
  </section>

  <section class="card card--banded col-3 row-3">
    <div class="band" style="top:7px;height:125px"></div>
    <div class="band" style="top:229px;height:117px"></div>
    <div class="ln head on-band" style="top:49px;font-size:40px">STARLET</div>
    <div class="ln head on-band" style="top:99px;font-size:40px">TRICKS</div>
    <div class="ln sub ruled" style="top:155px;font-size:17px;--rule:50px">TO A</div>
    <div class="ribbon ribbon--ink" style="left:40px;top:174px;width:203px;height:42px">
      <svg viewBox="0 0 200 50" preserveAspectRatio="none" aria-hidden="true">
        <polygon class="tail" points="2,12 40,12 40,48 2,48 12,30"/><polygon class="fold" points="26,40 40,40 40,48"/>
        <polygon class="tail" points="198,12 160,12 160,48 198,48 188,30"/><polygon class="fold" points="174,40 160,40 160,48"/>
        <rect class="band-fill" x="26" y="0" width="148" height="40"/>
      </svg>
      <span style="font-size:14px">SLENDER MIDLINE</span>
    </div>
    <div class="ln script on-band" style="top:262px;font-size:32px">Beyond 50</div>
    <div class="tag tag--solid" style="top:292px;height:27px;left:48px;right:48px">ZERO SCALPEL NEEDED</div>
  </section>

</main>
</body>
</html>
```